Creative way to lay out a career advancement graphic

Are you a designer with a knack for turning complex concepts into visually captivating masterpieces? We have an exciting project that needs your unique talent! We're on the lookout for a creative designer to help us visualize our company's diverse career paths. Our organization offers a plethora of opportunities in project management, engineering, sales, and more. We want to showcase these pathways in a visually engaging manner to empower potential job candidates with a clear understanding of their advancement options within our company. Design must be flexible and able to be edited.

Check out the attached examples of the positions we'd like to include in this visualization (doc "inside sales" are correct positions). Your task will be to transform this information into a visually stunning representation that's both informative and inspiring.
This project is not just about design—it's about shaping the narrative of career growth and opportunity within our organization. Your creative input will play a vital role in helping us attract top talent and communicate our company's commitment to fostering professional development. Brand guidelines are also attached for reference. The document titled "quarbel" demonstrates a badly done version of what we are trying to achieve. We want to denote multiple routes of advancement. You don't have to get the paths completely correct, you just need to show how it could be approached in a design. For example, A "submittal Specialist" could become a "project manager" but also could ascend to the role of "Industrial Estimator" if they want to move in that direction.

```html
<!DOCTYPE html>
<html lang="en">
<head>
<meta charset="utf-8">
<title>Varnell – Sales Development</title>
<link rel="stylesheet" href="https://fonts.googleapis.com/css2?family=Archivo+Black&family=Roboto:wght@700&family=Hind:wght@500&display=swap">
<style>
  :root {
    --navy: #07075f;
    --orange: #f5a800;
    --white: #ffffff;
    --paper: #ffffff;
  }
  * { margin: 0; padding: 0; box-sizing: border-box; }
  html, body { width: 1200px; height: 1046px; overflow: hidden; background: var(--paper); }
  .chart { position: relative; width: 1200px; height: 1046px; background: var(--paper); }
  .chart-lines { position: absolute; inset: 0; }

  .brand {
    position: absolute; left: 55px; top: 30px;
    color: var(--white);
  }
  .brand-name {
    display: flex; align-items: center; gap: 12px;
    font-family: "Archivo Black", sans-serif; font-size: 48px; line-height: 58px; letter-spacing: 1px;
  }
  .brand-dot { width: 22px; height: 22px; border-radius: 50%; background: var(--orange); }
  .brand-tagline {
    font-family: "Roboto", sans-serif; font-weight: 700; font-size: 13px;
    letter-spacing: 3.2px; margin-top: 6px;
  }
  .page-title {
    position: absolute; left: 458px; top: 39px; width: 720px;
    font-family: "Archivo Black", sans-serif; font-size: 54px; line-height: 60px;
    color: var(--white); letter-spacing: 1.2px; white-space: nowrap;
  }

  .role {
    position: absolute; width: 270px; text-align: center; color: var(--navy);
  }
  .role-title {
    font-family: "Roboto", sans-serif; font-weight: 700; font-size: 18.5px; line-height: 25px;
  }
  .role-duties {
    list-style: none; margin-top: 5px;
    font-family: "Hind", sans-serif; font-weight: 500; font-size: 11.5px; line-height: 19.5px;
    color: #111;
  }

  .flow-label {
    position: absolute; font-family: "Roboto", sans-serif; font-weight: 700;
    text-align: center; transform: translate(-50%, -50%); white-space: nowrap;
  }
  .flow-data { color: var(--white); font-family: "Archivo Black", sans-serif; font-size: 46px; }
  .flow-condition { color: var(--white); font-size: 26px; }
  .flow-process { font-size: 24px; }
  .flow-process.on-navy { color: var(--white); }
  .flow-process.on-orange { color: var(--navy); }
  .flow-branch { color: var(--navy); font-size: 14px; background: var(--paper); padding: 1px 2px; }
</style>
</head>
<body>
<main class="chart">
  <svg class="chart-lines" width="1200" height="1046" viewBox="0 0 1200 1046" aria-hidden="true">
    <rect class="header-strip" x="0" y="0" width="1200" height="20" fill="var(--navy)"/>
    <path class="header-band" d="M432,20 H1200 V120 H388 Q400,80 412,40 Q418,20 432,20 Z" fill="var(--orange)"/>
    <path class="header-brand" d="M0,0 H416 L388,120 Q370,144 340,144 H0 Z" fill="var(--navy)"/>
    <rect class="footer-strip" x="0" y="1034" width="1200" height="12" fill="var(--navy)"/>

    <g class="career-paths" fill="none" stroke="var(--orange)" stroke-width="1.6">
      <path d="M104,195 H90 Q60,195 60,225 V375 Q60,396 74,396"/>
      <path d="M260,195 H290 Q315,195 315,220 V315 Q315,345 345,345 H541 Q571,345 571,315 V225 Q571,195 601,195 H630"/>
      <path d="M801,195 H932"/>
      <path d="M842,404 Q861,410 861,430 V522 Q861,552 831,552 H90 Q60,552 60,582 V610 Q60,634 87,634"/>
      <path d="M826,637 Q861,640 861,665 V753 Q861,783 831,783 H90 Q60,783 60,813 V841 Q60,865 87,865"/>
      <path d="M282,865 H310 Q338,865 338,893 V958 Q338,988 368,988 H831 Q861,988 861,958 V893 Q861,865 826,865"/>
      <path d="M315,391 V512 M592,391 V512 M313,597 V739 M591,597 V739 M599,830 V937"/>
    </g>

    <g class="path-markers" fill="var(--orange)">
      <circle cx="104" cy="195" r="3"/><circle cx="74" cy="396" r="3"/>
      <circle cx="260" cy="195" r="3"/><circle cx="630" cy="195" r="3"/>
      <circle cx="801" cy="195" r="3"/><circle cx="932" cy="195" r="3"/>
      <circle cx="842" cy="404" r="3"/><circle cx="87" cy="634" r="3"/>
      <circle cx="826" cy="637" r="3"/><circle cx="87" cy="865" r="3"/>
      <circle cx="282" cy="865" r="3"/><circle cx="826" cy="865" r="3"/>
      <circle cx="315" cy="391" r="3"/><circle cx="315" cy="512" r="3"/>
      <circle cx="592" cy="391" r="3"/><circle cx="592" cy="512" r="3"/>
      <circle cx="313" cy="597" r="3"/><circle cx="313" cy="739" r="3"/>
      <circle cx="591" cy="597" r="3"/><circle cx="591" cy="739" r="3"/>
      <circle cx="599" cy="830" r="3"/><circle cx="599" cy="937" r="3"/>

      <polygon points="55,301 60,292 65,301"/>
      <polygon points="310,260 320,260 315,269"/>
      <polygon points="438,340 447,345 438,350"/>
      <polygon points="566,270 571,261 576,270"/>
      <polygon points="856,477 861,468 866,477"/>
      <polygon points="346,547 355,552 346,557"/>
      <polygon points="638,547 647,552 638,557"/>
      <polygon points="55,596 60,587 65,596"/>
      <polygon points="856,713 861,704 866,713"/>
      <polygon points="346,778 355,783 346,788"/>
      <polygon points="638,778 647,783 638,788"/>
      <polygon points="55,829 60,820 65,829"/>
      <polygon points="333,928 338,919 343,928"/>
      <polygon points="604,983 595,988 604,993"/>
      <polygon points="856,920 861,929 866,920"/>

      <polygon points="306,452 312,446 312,458"/><polygon points="324,452 318,446 318,458"/>
      <polygon points="583,452 589,446 589,458"/><polygon points="601,452 595,446 595,458"/>
      <polygon points="304,668 310,662 310,674"/><polygon points="322,668 316,662 316,674"/>
      <polygon points="582,668 588,662 588,674"/><polygon points="600,668 594,662 594,674"/>
      <polygon points="590,883 596,877 596,889"/><polygon points="608,883 602,877 602,889"/>
    </g>

    <rect class="flow-data-box" x="950" y="158" width="160" height="79" rx="10" fill="var(--navy)"/>
    <ellipse class="flow-condition-shape" cx="1030" cy="406" rx="104" ry="69" fill="var(--orange)"/>
    <circle cx="1030" cy="647" r="76" fill="none" stroke="var(--navy)" stroke-width="1.6" stroke-dasharray="1.5 3"/>
    <circle class="flow-process-navy" cx="1030" cy="647" r="70" fill="var(--navy)"/>
    <circle cx="1030" cy="900" r="76" fill="none" stroke="var(--navy)" stroke-width="1.6" stroke-dasharray="1.5 3"/>
    <circle class="flow-process-orange" cx="1030" cy="900" r="70" fill="var(--orange)"/>
    <g fill="none" stroke="var(--navy)" stroke-width="1.5" stroke-dasharray="5 4">
      <path d="M1030,240 V334"/>
      <path d="M1030,478 V508 M1030,530 V561"/>
      <path d="M1030,726 V812"/>
      <path d="M1085,468 Q1140,540 1136,630 Q1134,760 1094,827"/>
    </g>
    <g fill="var(--orange)">
      <polygon points="1024,562 1036,562 1030,570"/>
      <polygon points="1024,813 1036,813 1030,821"/>
      <polygon points="1086,826 1097,832 1087,838"/>
    </g>
  </svg>

  <header>
    <div class="brand">
      <div class="brand-name"><span class="brand-dot"></span>VARNELL</div>
      <div class="brand-tagline">Power and Controls Group</div>
    </div>
    <h1 class="page-title">SALES DEVELOPMENT</h1>
  </header>

  <section class="role" style="left:47px; top:183px;">
    <h2 class="role-title">Outside Sales</h2>
    <ul class="role-duties"><li>Prospecting and lead generation</li><li>Building and maintaining relationships</li><li>Closing sales and achieving targets</li></ul>
  </section>
  <section class="role" style="left:305px; top:183px;">
    <h2 class="role-title">Sales Leadership</h2>
    <ul class="role-duties"><li>Sets sets goals and targets</li><li>Sales team supervision, mentoring,</li><li>training and coaching</li><li>Sales strategy development and</li><li>implementation</li></ul>
  </section>
  <section class="role" style="left:580px; top:181px;">
    <h2 class="role-title">Vice President,<br>Sales</h2>
    <ul class="role-duties"><li>Sales strategy development</li><li>Revenue generation</li><li>Market analysis</li><li>Sales forecasting and budgeting</li><li>Team Leadership</li></ul>
  </section>

  <section class="role" style="left:51px; top:389px;">
    <h2 class="role-title">Lead Project Manager</h2>
    <ul class="role-duties"><li>Team leadership, mentoring and training</li><li>Project planning and organization</li><li>Monitoring and control</li><li>Customer service and communication</li><li>Continuous improvement</li></ul>
  </section>
  <section class="role" style="left:319px; top:389px;">
    <h2 class="role-title">Lead Technical Engineer</h2>
    <ul class="role-duties"><li>Team leadership, mentoring and training</li><li>Technical sales liaison</li><li>Influence specifications</li><li>Read &amp; interpret specifications</li></ul>
  </section>
  <section class="role" style="left:587px; top:389px;">
    <h2 class="role-title">Lead Project Engineer</h2>
    <ul class="role-duties"><li>Team leadership, mentoring and training</li><li>Technical expertise + engineering support</li><li>Subject matter expert relating to job,</li><li>equipment and commissioning</li><li>Quality control and project execution</li><li>Continuous improvement</li></ul>
  </section>

  <section class="role" style="left:46px; top:622px;">
    <h2 class="role-title">Project Manager</h2>
    <ul class="role-duties"><li>Project planning and organization</li><li>Monitoring and control</li><li>Customer service and communication</li></ul>
  </section>
  <section class="role" style="left:316px; top:595px;">
    <h2 class="role-title">Industrial<br>Estimator (Senior)</h2>
    <ul class="role-duties"><li>Quote preparation for more complex jobs</li><li>Specification and drawing review</li><li>Customer and vendor relationship</li><li>Analyze competitive pricing</li><li>Support outside sales</li></ul>
  </section>
  <section class="role" style="left:593px; top:622px;">
    <h2 class="role-title">Project Engineer</h2>
    <ul class="role-duties"><li>Technical expertise + engineering Support</li><li>Subject matter expert relating to job,</li><li>equipment and commissioning</li><li>Quality control and project execution</li></ul>
  </section>

  <section class="role" style="left:47px; top:823px;">
    <h2 class="role-title">Industrial<br>Estimator (Junior)</h2>
    <ul class="role-duties"><li>Quote preparation for less complex jobs</li><li>Specification and drawing Review</li><li>Vendor relationship</li><li>Support outside sales</li></ul>
  </section>
  <section class="role" style="left:337px; top:823px;">
    <h2 class="role-title">Submittal<br>Specialist</h2>
    <ul class="role-duties"><li>Document control and management</li><li>Submittal preparation and review</li><li>Communication and coordination</li></ul>
  </section>
  <section class="role" style="left:593px; top:823px;">
    <h2 class="role-title">Project Coordinator<br>(Gatekeeper)</h2>
    <ul class="role-duties"><li>Data entry for projects</li><li>Reviews project complexity</li><li>and assigns accordingly</li></ul>
  </section>

  <div class="flow-label flow-data" style="left:1030px; top:198px;">DATA</div>
  <div class="flow-label flow-condition" style="left:1030px; top:406px;">Condition?</div>
  <div class="flow-label flow-branch" style="left:1030px; top:519px;">No</div>
  <div class="flow-label flow-branch" style="left:1137px; top:643px;">Yes</div>
  <div class="flow-label flow-process on-navy" style="left:1030px; top:647px;">Process</div>
  <div class="flow-label flow-process on-orange" style="left:1030px; top:900px;">Process</div>
</main>
</body>
</html>
```